Trim Path Studio needs A4 information sheets that vibrant and easy to read with a healthy food...

I have written an introduction an "About Me " and 4 pages of material that will be uploaded on my website "Trim Path Studio" but I am not a designer and it looks boring. I need the information to remain unchanged but the presentation to look better, The logo was designed through Artboard Hive. The text could be moew interesting, Introduction page has NO …… NO...… etc these could be scattered or high lighted. There could be healthy food symbols in the margins etc

Colors
3176b5
add136
fbf286

Requirements
Must have
• The content must not be changed just the presentation.
Nice to have
• Colour . Symbols of foods such as fruits, vegetables, fish , seafood ,
Should not have
• Any high fat foods , fast foods,
• NO REFERENCE TO GYMS OR EXCERCISE THIS IS JUST ABOUT FOOD.

```html
<!DOCTYPE html>
<html lang="en">
<head>
<meta charset="utf-8">
<title>Foods To Avoid – Trim Path Studio</title>
<link rel="stylesheet" href="https://fonts.googleapis.com/css2?family=Oswald:wght@300;400;700&family=Open+Sans:wght@400;600;700&display=swap">
<style>
:root{
  --green:#8cc63f;
  --green-dark:#6ea92c;
  --orange:#f7941d;
  --text:#3a3a3a;
  --white:#ffffff;
  --cream:#fbf286;
  --blue:#3176b5;
}
*{margin:0;padding:0;box-sizing:border-box}
html,body{width:849px;height:1200px;overflow:hidden;background:var(--white)}
.sheet{position:relative;width:849px;height:1200px;overflow:hidden;font-family:"Open Sans",Arial,sans-serif;color:var(--text)}
.hero{position:absolute;left:0;top:0;width:849px;height:240px;background:var(--white)}
.hero-band{position:absolute;left:0;top:0;width:600px;height:240px;background:var(--green);border-bottom-right-radius:40px}
.hero-title{position:absolute;left:55px;top:28px;font-family:"Oswald",Arial,sans-serif;font-weight:700;color:var(--white);font-size:92px;line-height:88px;letter-spacing:1px}
.fries-art{position:absolute;left:590px;top:0;width:240px;height:225px;border-radius:0 0 20px 20px;background:linear-gradient(180deg,#f9d24a,#f0a91d 70%,#e2372b 70%)}
.intro-strip{position:absolute;left:0;top:236px;width:849px;height:62px;background:var(--orange);padding:8px 40px 0 55px;color:var(--white);font-family:"Oswald",Arial,sans-serif;font-weight:400;font-size:19px;line-height:23px;text-transform:uppercase}
.section-title{position:absolute;font-family:"Oswald",Arial,sans-serif;font-weight:300;font-size:44px;letter-spacing:1px;text-transform:uppercase}
.fat-title{left:55px;top:315px;color:var(--green)}
.dessert-art{position:absolute;left:560px;top:290px;width:270px;height:125px;border-radius:14px;background:linear-gradient(90deg,#fbeec9 0%,#f6d98c 40%,#6b3a1e 60%,#3e1f0c 100%)}
.check-list{position:absolute;list-style:none;font-size:14px;line-height:19px}
.check-list li{position:relative;padding-left:30px;margin-bottom:11px}
.check-list svg{position:absolute;left:0;top:1px;width:18px;height:18px}
.fat-left{left:55px;top:430px;width:330px}
.fat-right{left:420px;top:430px;width:390px}
.sugar-band{position:absolute;left:0;top:872px;width:849px;height:78px;background:var(--green)}
.sugar-underline{position:absolute;left:0;top:950px;width:849px;height:10px;background:var(--orange)}
.sugar-title{left:55px;top:878px;color:var(--white);font-weight:400}
.sugar-art{position:absolute;left:650px;top:890px;width:199px;height:300px;background:linear-gradient(180deg,#e2372b 0%,#c8261c 45%,#f2f2f2 45%,#dcdcdc 100%)}
.sugar-left{left:55px;top:985px;width:270px}
.sugar-right{left:345px;top:985px;width:290px}
.brand{position:absolute;left:40px;top:1140px;display:flex;align-items:center;gap:8px;font-family:"Open Sans",Arial,sans-serif;font-weight:700;font-size:13px;color:var(--green-dark)}
.brand-dot{width:22px;height:22px;border-radius:50%;background:var(--green)}
.ants-art{position:absolute;left:180px;top:1170px;width:460px;height:14px;background:linear-gradient(90deg,rgba(60,40,20,.15),rgba(60,40,20,.3),rgba(60,40,20,.15));border-radius:7px}
</style>
</head>
<body>
<div class="sheet">
  <header class="hero">
    <div class="hero-band"></div>
    <h1 class="hero-title">FOODS<br>TO AVOID</h1>
    <div class="fries-art" role="img" aria-label="Carton of french fries illustration"></div>
  </header>
  <p class="intro-strip">The following foods should be<br>avoided if trying to lose weight.</p>

  <h2 class="section-title fat-title">High Fat Foods</h2>
  <div class="dessert-art" role="img" aria-label="Illustration of a cupcake with cream and chocolate brownies"></div>

  <svg width="0" height="0" style="position:absolute">
    <symbol id="tick" viewBox="0 0 20 20"><circle cx="10" cy="10" r="8.5" fill="none" stroke="#8cc63f" stroke-width="1.6"/><path d="M6 10.3l2.8 2.7L14.2 7.3" fill="none" stroke="#8cc63f" stroke-width="1.8" stroke-linecap="round" stroke-linejoin="round"/></symbol>
  </svg>

  <ul class="check-list fat-left">
    <li><svg><use href="#tick"/></svg>All Oils Including Olive and Canola Oil (use spray)</li>
    <li><svg><use href="#tick"/></svg>All forms of Margarine and Butter (scrape or none on bread, none added to vegetables, none used in cooking.</li>
    <li><svg><use href="#tick"/></svg>All take away foods except Sandwiches without Butter and with low fat fillings.</li>
    <li><svg><use href="#tick"/></svg>Pies, Pastry, Sausage Rolls</li>
    <li><svg><use href="#tick"/></svg>Fried Foods Such As Chips, Fried Fish.</li>
    <li><svg><use href="#tick"/></svg>Fatty Cuts of Meat, Luncheon Meats, Sausages, Salami, Crumbed Meats, Frankfurts, Rissoles, Skin of Chicken, Marinated Kebabs.</li>
  </ul>
  <ul class="check-list fat-right">
    <li><svg><use href="#tick"/></svg>Frozen foods that are crumbed or pre-fried such as crumbed fish and oven fried chips, Quiche, Pre prepared meals such as lasagne (unless a “diet” meal)</li>
    <li><svg><use href="#tick"/></svg>Baked Vegetables Unless Baked With Oil Spray.</li>
    <li><svg><use href="#tick"/></svg>Cream Cheese and Cheese Spread</li>
    <li><svg><use href="#tick"/></svg>Nuts And Peanut Butter (unless vegetarian)</li>
    <li><svg><use href="#tick"/></svg>Crisps, Chips, Krunchy Curls Etc.</li>
    <li><svg><use href="#tick"/></svg>Full Fat Mayonnaise or Salad Dressings.</li>
    <li><svg><use href="#tick"/></svg>Health Food Bars eg. Muesli Bars and Nut Bars</li>
    <li><svg><use href="#tick"/></svg>Chocolate, Fudge, Caramel Ice Cream and Cream</li>
    <li><svg><use href="#tick"/></svg>Sweet Biscuits, Shortbread Biscuits, Cake, Crispos</li>
  </ul>

  <div class="sugar-band"></div>
  <div class="sugar-underline"></div>
  <h2 class="section-title sugar-title">High Sugar Foods</h2>
  <div class="sugar-art" role="img" aria-label="Illustration of a soft drink cup and a pile of sugar cubes"></div>

  <ul class="check-list sugar-left">
    <li><svg><use href="#tick"/></svg>Soft Drink and Cordial Unless Diet or Sugar Free.</li>
    <li><svg><use href="#tick"/></svg>Tonic Water Unless “Diet”</li>
    <li><svg><use href="#tick"/></svg>Fruit Juice Drink. (not too much pure fruit juice either!)</li>
  </ul>
  <ul class="check-list sugar-right">
    <li><svg><use href="#tick"/></svg>Tinned Fruit in Syrup, Jelly Unless Diet, Desserts</li>
    <li><svg><use href="#tick"/></svg>Lollies, Jubes etc</li>
    <li><svg><use href="#tick"/></svg>Alcohol (It is not all bad news. See Maya’s video for a balanced approach)</li>
    <li><svg><use href="#tick"/></svg>Glace Fruit, Dried Fruit</li>
  </ul>

  <div class="brand"><span class="brand-dot"></span>Trim Path Studio</div>
  <div class="ants-art" role="img" aria-label="Line of small ants marching along the bottom edge"></div>
</div>
</body>
</html>
```